Bruntel general construction

We need an website that are similar to these websites:
https://www.morvexa.com/en/
https://dulnari.com/company/

but with a tweak. Do not copy the entire website but atleast similar and yet better than them.

For reference this our current website.
https://bruntel.ph/

For the winning Designer please help us with the migration from our old website to the new redesign website.

```html
<!DOCTYPE html>
<html lang="en">
<head>
<meta charset="utf-8">
<title>Bruntel — One Step Ahead in Industrial Services</title>
<link rel="stylesheet" href="https://fonts.googleapis.com/css2?family=Inter:wght@400;500;600;700;800&family=Montserrat:wght@300&display=swap">
<style>
:root{
  --red:#c8102e;
  --ink:#2b2b2b;
  --text:#555;
  --muted:#777;
  --light:#f0f0f0;
  --white:#fff;
  --footer:#222;
  --footer-line:#333;
  --orange:rgba(214,110,40,.72);
}
*{box-sizing:border-box;margin:0;padding:0}
html,body{width:1200px;height:3846px;overflow:hidden}
body{font-family:'Inter',sans-serif;color:var(--ink);background:var(--white);position:relative}
a{color:inherit;text-decoration:none}

/* Header */
.site-header{position:absolute;top:0;left:0;width:1200px;height:72px;background:var(--white);border-bottom:1px solid #e6e6e6}
.brand{position:absolute;left:24px;top:22px;display:flex;align-items:center;gap:6px;font-weight:700;font-size:13px;color:var(--red)}
.brand-dot{width:12px;height:12px;border-radius:50%;background:#f2a21b}
.main-nav{position:absolute;left:233px;top:0;display:flex;gap:29px;height:72px;align-items:center}
.main-nav a{font-size:11px;font-weight:500;letter-spacing:.6px;color:#333;position:relative;height:72px;line-height:72px}
.main-nav a.active::after{content:"";position:absolute;left:0;right:0;bottom:2px;height:2px;background:var(--red)}
.theme{position:absolute;left:978px;top:29px;font-size:10px;color:#999;letter-spacing:.6px}
.theme-toggle{position:absolute;left:1040px;top:20px;width:30px;height:30px;border-radius:50%;background:#f1f1f1;display:flex;align-items:center;justify-content:center}
.header-cta{position:absolute;left:1083px;top:19px;width:90px;height:33px;border:1px solid #ddd;font-size:10px;font-weight:600;letter-spacing:.8px;display:flex;align-items:center;justify-content:center}

/* Hero */
.hero{position:absolute;top:72px;left:0;width:1200px;height:500px;background:linear-gradient(100deg,#5b4a3a 0%,#8a7a66 35%,#b3aa9e 65%,#6d6a65 100%)}
.hero-panel{position:absolute;left:67px;top:59px;width:340px;height:391px;background:var(--orange);border-radius:4px;display:flex;align-items:center;justify-content:center;padding:0 22px}
.hero-panel p{font-family:'Montserrat',sans-serif;font-weight:300;font-size:21px;line-height:29px;color:rgba(255,255,255,.6);text-align:center}
.hero-title{position:absolute;left:0;width:1200px;top:118px;text-align:center;font-weight:800;font-size:60px;color:var(--white);letter-spacing:-.5px}
.hero-tag{position:absolute;left:0;width:1200px;top:206px;text-align:center;font-size:19px;color:var(--white)}
.hero-btn{position:absolute;left:478px;top:261px;width:246px;height:45px;background:var(--red);color:var(--white);font-size:12px;font-weight:700;letter-spacing:.9px;display:flex;align-items:center;justify-content:center}
.hero-bars{position:absolute;left:67px;top:454px;display:flex;gap:10px}
.hero-bars span{width:84px;height:8px;border-radius:4px}
.hero-dots{position:absolute;left:566px;top:453px;display:flex;gap:10px}
.hero-dots span{width:10px;height:10px;border-radius:50%;border:1.5px solid #fff}
.hero-dots span.on{background:var(--red);border-color:var(--red)}

/* Intro */
.intro{position:absolute;top:572px;left:0;width:1200px;height:253px;text-align:center}
.intro h2{margin-top:70px;font-size:37px;font-weight:800;letter-spacing:-.3px;color:#2e2e2e}
.intro p{width:700px;margin:24px auto 0;font-size:15px;line-height:27px;color:var(--muted)}

/* Section head */
.section-head{text-align:center}
.section-head h2{font-size:43px;font-weight:800;color:#2e2e2e;letter-spacing:-.3px}
.section-head .rule{width:54px;height:3px;background:var(--red);margin:24px auto 0}

.updates{position:absolute;top:825px;left:0;width:1200px;height:602px;background:var(--light)}
.updates .section-head{padding-top:82px}
.news-section{position:absolute;top:2761px;left:0;width:1200px;height:681px;background:var(--white)}
.news-section .section-head{padding-top:81px}

.card-grid{position:absolute;left:84px;display:flex;gap:27px}
.card{width:326px}
.card-media{width:326px;height:182px}
.card-date{margin-top:21px;font-size:11px;font-weight:600;color:var(--red);letter-spacing:.8px}
.card-title{margin-top:9px;font-size:16px;font-weight:600;line-height:21px;color:#2e2e2e;padding-right:12px}
.card-link{margin-top:14px;font-size:11px;font-weight:700;color:var(--red);letter-spacing:.8px;display:flex;align-items:center;gap:6px}

/* Feature bands */
.feature{position:absolute;left:0;width:1200px;color:var(--white)}
.feature h2{font-size:39px;font-weight:800;line-height:60px;letter-spacing:-.3px}
.feature p{font-size:16px;line-height:27.5px;margin-top:18px;color:rgba(255,255,255,.92)}
.outline-btn{display:inline-flex;align-items:center;gap:10px;margin-top:24px;height:42px;padding:0 26px;border:2px solid var(--white);font-size:12px;font-weight:700;letter-spacing:.8px}
.feature-body{position:absolute}

/* Footer */
.site-footer{position:absolute;top:3442px;left:0;width:1200px;height:404px;background:var(--footer);color:#ddd}
.foot-brand{position:absolute;left:84px;top:56px;display:flex;align-items:center;gap:6px;font-size:14px;font-weight:700;color:var(--white)}
.foot-tag{position:absolute;left:84px;top:118px;font-size:12px;letter-spacing:1.2px;color:#ddd}
.foot-col{position:absolute;top:57px}
.foot-col h4{font-size:11px;font-weight:700;letter-spacing:1.3px;color:var(--white);margin-bottom:26px}
.foot-col li{list-style:none;font-size:12px;color:#ddd;margin-bottom:17px;line-height:14px}
.foot-col .addr{line-height:22px;margin-bottom:12px}
.socials{position:absolute;left:84px;top:305px;display:flex;gap:13px}
.socials span{width:34px;height:34px;border-radius:50%;border:1px solid #555}
.foot-rule{position:absolute;left:0;top:348px;width:1200px;height:1px;background:var(--footer-line)}
.copyright{position:absolute;left:0;top:368px;width:1200px;text-align:center;font-size:11px;color:#888}
</style>
</head>
<body>

<header class="site-header">
  <a class="brand" href="#"><span class="brand-dot"></span>Bruntel</a>
  <nav class="main-nav">
    <a class="active" href="#">HOME</a>
    <a href="#">ABOUT US</a>
    <a href="#">OUR SERVICES</a>
    <a href="#">OUR TEAM</a>
    <a href="#">NEWS &amp; MEDIA</a>
    <a href="#">CONTACT US</a>
  </nav>
  <span class="theme">THEME :</span>
  <span class="theme-toggle">
    <svg width="14" height="14" viewBox="0 0 14 14"><circle cx="7" cy="7" r="3" fill="#333"/><g stroke="#333" stroke-width="1.4" stroke-linecap="round"><line x1="7" y1="0.8" x2="7" y2="2.2"/><line x1="7" y1="11.8" x2="7" y2="13.2"/><line x1="0.8" y1="7" x2="2.2" y2="7"/><line x1="11.8" y1="7" x2="13.2" y2="7"/><line x1="2.6" y1="2.6" x2="3.6" y2="3.6"/><line x1="10.4" y1="10.4" x2="11.4" y2="11.4"/><line x1="2.6" y1="11.4" x2="3.6" y2="10.4"/><line x1="10.4" y1="3.6" x2="11.4" y2="2.6"/></g></svg>
  </span>
  <a class="header-cta" href="#">CONTACT</a>
</header>

<section class="hero" role="img" aria-label="Construction site at dusk with cranes, a white safety helmet and rolled blueprints on a desk">
  <div class="hero-panel"><p>We value the training of our people and enhance our reputation as a leading contractor in the construction, industrial, and oil and gas sectors while providing remarkable support services for repair and maintenance projects.</p></div>
  <h1 class="hero-title">BRUNTEL</h1>
  <p class="hero-tag">One Step Ahead in Industrial Services</p>
  <a class="hero-btn" href="#">DISCOVER OUR SERVICES</a>
  <div class="hero-bars"><span style="background:#2a7fc4"></span><span style="background:#2a7fc4"></span><span style="background:#d9641e"></span><span style="background:#e3a51c"></span><span style="background:#e8c21a"></span></div>
  <div class="hero-dots"><span></span><span></span><span></span><span class="on"></span></div>
</section>

<section class="intro">
  <h2>TRUSTED TO DELIVER QUALITY INDUSTRIAL SERVICES</h2>
  <p>Our ability to deliver a quality product has given us the reputation to position ourselves as a leading contractor in the sectors and industries that we serve</p>
</section>

<section class="updates">
  <div class="section-head"><h2>WHAT'S UP AT BRUNTEL</h2><div class="rule"></div></div>
  <div class="card-grid" style="top:214px">
    <article class="card">
      <div class="card-media" role="img" aria-label="Hazy city skyline seen from a waterfront promenade with flower beds" style="background:linear-gradient(180deg,#c9cccd 0%,#a9adad 60%,#6c6f52 100%)"></div>
      <div class="card-date">JAN 2024</div>
      <h3 class="card-title">Environmental Protection Industry A Job Creator</h3>
      <a class="card-link" href="#">READ <svg width="10" height="10" viewBox="0 0 10 10"><path d="M1 5h7M5 2l3 3-3 3" stroke="currentColor" stroke-width="1.5" fill="none"/></svg></a>
    </article>
    <article class="card">
      <div class="card-media" role="img" aria-label="Illuminated gas processing plant under an evening sky" style="background:linear-gradient(180deg,#1d3d78 0%,#385a8c 55%,#6b6a60 100%)"></div>
      <div class="card-date">MAR 2024</div>
      <h3 class="card-title">Energy Recovery To Supply Turbocharger Technology</h3>
      <a class="card-link" href="#">READ <svg width="10" height="10" viewBox="0 0 10 10"><path d="M1 5h7M5 2l3 3-3 3" stroke="currentColor" stroke-width="1.5" fill="none"/></svg></a>
    </article>
    <article class="card">
      <div class="card-media" role="img" aria-label="Oilfield crew in blue coveralls working on a drilling rig floor" style="background:linear-gradient(135deg,#8fa3b5 0%,#3d5a86 45%,#b25a32 100%)"></div>
      <div class="card-date">JUN 2024</div>
      <h3 class="card-title">Positive Signs for Oilfield Services Sector</h3>
      <a class="card-link" href="#">READ <svg width="10" height="10" viewBox="0 0 10 10"><path d="M1 5h7M5 2l3 3-3 3" stroke="currentColor" stroke-width="1.5" fill="none"/></svg></a>
    </article>
  </div>
</section>

<section class="feature" style="top:1427px;height:445px;background:linear-gradient(180deg,#2e3d5c 0%,#334263 60%,#2c3755 100%)" role="img" aria-label="Industrial storage tanks and refinery at dusk under a blue overlay">
  <div class="feature-body" style="left:54px;top:88px;width:430px">
    <h2>OUR EXPERTISE</h2>
    <p>With decades of experience across multiple industries, Bruntel delivers comprehensive industrial services that meet the highest international standards. Our commitment to safety, quality, and innovation drives everything we do.</p>
    <a class="outline-btn" href="#">LEARN MORE <svg width="10" height="10" viewBox="0 0 10 10"><path d="M1 5h7M5 2l3 3-3 3" stroke="#fff" stroke-width="1.5" fill="none"/></svg></a>
  </div>
</section>

<section class="feature" style="top:1872px;height:512px;background:linear-gradient(180deg,#34415e 0%,#3d4a66 55%,#2f3b55 100%)" role="img" aria-label="Wind turbine on green hills with mountains behind under a blue overlay">
  <div class="feature-body" style="left:720px;top:72px;width:430px">
    <h2>ENVIRONMENTAL<br>PROTECTION</h2>
    <p>We have in-house expertise for the processing of both municipal and industrial solid wastes by adopting the latest technologies. These wastes can be converted to energy in the form of electrical power.</p>
    <a class="outline-btn" href="#">LEARN MORE <svg width="10" height="10" viewBox="0 0 10 10"><path d="M1 5h7M5 2l3 3-3 3" stroke="#fff" stroke-width="1.5" fill="none"/></svg></a>
  </div>
</section>

<section class="feature" style="top:2384px;height:377px;background:linear-gradient(180deg,#2f3a55 0%,#353f58 60%,#2a3249 100%)" role="img" aria-label="Water treatment plant and city skyline under a dark blue overlay">
  <div class="feature-body" style="left:54px;top:32px;width:410px">
    <h2>WATER TREATMENT</h2>
    <p>We have in-house expertise for the construction of Sewage Water Treatment Plants (SWTP) and utility desalination plants for the conversion of seawater to potable water.</p>
    <a class="outline-btn" href="#">LEARN MORE <svg width="10" height="10" viewBox="0 0 10 10"><path d="M1 5h7M5 2l3 3-3 3" stroke="#fff" stroke-width="1.5" fill="none"/></svg></a>
  </div>
</section>

<section class="news-section">
  <div class="section-head"><h2>LATEST NEWS</h2><div class="rule"></div></div>
  <div class="card-grid" style="top:214px">
    <article class="card">
      <div class="card-media" role="img" aria-label="Two engineers in hard hats and safety vests inspecting a building frame" style="background:linear-gradient(180deg,#e8e8e6 0%,#c9c4bc 55%,#4a6a9a 80%,#3a5d94 100%)"></div>
      <div class="card-date">FEB 2024</div>
      <h3 class="card-title">Climate Change Risk Management</h3>
      <a class="card-link" href="#">READ <svg width="10" height="10" viewBox="0 0 10 10"><path d="M1 5h7M5 2l3 3-3 3" stroke="currentColor" stroke-width="1.5" fill="none"/></svg></a>
    </article>
    <article class="card">
      <div class="card-media" role="img" aria-label="Sustainability sticker on a teal vehicle panel" style="background:linear-gradient(135deg,#1f4a55 0%,#2f6670 50%,#1a3940 100%)"></div>
      <div class="card-date">APR 2024</div>
      <h3 class="card-title">Retail Giants Talk Risk and Supply Chains</h3>
      <a class="card-link" href="#">READ <svg width="10" height="10" viewBox="0 0 10 10"><path d="M1 5h7M5 2l3 3-3 3" stroke="currentColor" stroke-width="1.5" fill="none"/></svg></a>
    </article>
    <article class="card">
      <div class="card-media" role="img" aria-label="Hand lifting a large water bottle against a sunset" style="background:linear-gradient(90deg,#111 0%,#1a1a1a 30%,#d9a22a 55%,#e7b63c 75%,#6a5a2a 100%)"></div>
      <div class="card-date">MAY 2024</div>
      <h3 class="card-title">New Regional Recycled Water<br>Programme</h3>
      <a class="card-link" href="#">READ <svg width="10" height="10" viewBox="0 0 10 10"><path d="M1 5h7M5 2l3 3-3 3" stroke="currentColor" stroke-width="1.5" fill="none"/></svg></a>
    </article>
  </div>
</section>

<footer class="site-footer">
  <div class="foot-brand"><span class="brand-dot"></span>Bruntel</div>
  <div class="foot-tag">ONE STEP AHEAD</div>
  <div class="foot-col" style="left:384px">
    <h4>QUICK LINKS</h4>
    <ul><li>About Us</li><li>Our Services</li><li>Our Team</li><li>News &amp; Media</li><li>Contact Us</li></ul>
  </div>
  <div class="foot-col" style="left:639px">
    <h4>SERVICES</h4>
    <ul><li>Environmental Protection</li><li>Power Generation</li><li>Water Treatment</li><li>Construction</li><li>Oil and Gas</li></ul>
  </div>
  <div class="foot-col" style="left:896px;width:220px">
    <h4>CONTACT</h4>
    <ul><li class="addr">14 Mabini Ridge Ave.<br>Brgy. Luntian, Marcelo City,<br>Cavite Philippines 4120</li><li>+63 (0) 46 555-0148</li><li>+63 (0) 917-555-0172</li><li>info@bruntel.com.ph</li></ul>
  </div>
  <div class="socials"><span></span><span></span><span></span></div>
  <div class="foot-rule"></div>
  <div class="copyright">Bruntel © 2024 All rights reserved</div>
</footer>

</body>
</html>
```